High-end Investment firm website

It needs to feel very high-end. We like clean design which incorporates a good deal of white space with the use of imagery to be provided.

Here are a few examples of design which is appealing:
https://www.corlandholdings.example
https://www.brevikcapital.example

Please use the following shade of blue in the design #7BAFD4.

Additional brand colors black, grey and white.

This google doc has a link to all of the content for the site. It also has detailed design notes per section.

https://files.quenderpad.example/doc/7TRaM2pLwe9XnqBv4KcYh0sJd8FgU3oZi5EtNm1Qx/edit?usp=sharing

Target Market(s)

Investors and companies in our target industries

Industry/Entity Type

Investment

Coding

Coded - Design and coding required

Number of Pages Required

5+ page

Font styles to use
Sans Serif

Requirements
Must have
• Clean feel, lots of white space.
Nice to have
• Clean graphics similar to https://www.corlandholdings.example

```html
<!DOCTYPE html>
<html lang="en">
<head>
<meta charset="utf-8">
<title>Meridane Industries</title>
<link href="https://fonts.googleapis.com/css2?family=Arimo:wght@400;700&family=Open+Sans:wght@400;600&display=swap" rel="stylesheet">
<style>
:root{
  --navy:#0f2a44;
  --navy-deep:#0b2038;
  --brand-blue:#7BAFD4;
  --steel:#2a6d9e;
  --wing:#3b4650;
  --ink:#1b1b1b;
  --light:#f3f5f8;
  --white:#fff;
}
*{margin:0;padding:0;box-sizing:border-box}
html,body{width:1200px;height:4045px;overflow:hidden}
body{position:relative;font-family:"Arimo",Arial,sans-serif;color:var(--ink);background:var(--white)}
.abs{position:absolute}
.topbar{left:0;top:0;width:1200px;height:49px;background:var(--navy);color:var(--white);font-size:17px}
.topbar .item{top:14px;display:flex;align-items:center;gap:10px}
.topbar .divider{left:274px;top:10px;width:1px;height:30px;background:rgba(255,255,255,.5)}
.social-dot{width:32px;height:32px;border:2px solid var(--white);border-radius:50%}
.header{left:0;top:49px;width:1200px;height:122px;background:var(--white)}
.brand{left:190px;top:12px;width:170px;text-align:center}
.brand-mark{width:44px;height:44px;background:var(--steel);margin:0 auto 6px}
.brand-name{font-size:26px;color:var(--navy);letter-spacing:1px}
.brand-sub{font-size:10px;letter-spacing:3px;color:var(--steel);border-top:1px solid var(--steel);margin-top:2px}
.nav{top:58px;font-size:17px;color:var(--navy);display:flex;align-items:center;gap:6px}
.chev{width:7px;height:7px;border-right:1.5px solid var(--navy);border-bottom:1.5px solid var(--navy);transform:rotate(45deg);margin-top:-4px}
.hero{left:0;top:171px;width:1200px;height:549px;background:linear-gradient(180deg,#9fb3c8 0%,#55708f 45%,#1d3553 100%)}
.hero h1{position:absolute;left:0;top:214px;width:1200px;text-align:center;color:var(--white);font-size:41px;line-height:66px;font-weight:700;text-shadow:0 3px 4px rgba(0,0,0,.55)}
.section-title{font-weight:700;font-size:35px}
.about-title{left:152px;top:826px;color:var(--navy)}
.about-text{left:152px;top:886px;width:514px;font-size:15px;line-height:34.5px;text-align:justify;color:#222}
.about-frame{left:765px;top:814px;width:324px;height:336px;background:var(--steel)}
.about-photo{left:738px;top:800px;width:322px;height:334px;background:linear-gradient(135deg,#b8a27a,#6a8a4a 50%,#5a5f63)}
.focus{left:0;top:1207px;width:1200px;height:704px;background:linear-gradient(180deg,#5b85b6,#6b94c4)}
.focus-title{left:0;top:1270px;width:1200px;text-align:center;color:var(--white)}
.focus-item{width:260px;text-align:center;color:var(--white);font-size:27px}
.focus-ring{width:120px;height:120px;border-radius:50%;background:var(--white);border:9px solid var(--navy-deep);margin:0 auto 26px;display:flex;align-items:center;justify-content:center}
.statement-photo{left:149px;top:1991px;width:276px;height:276px;border-radius:50%;background:linear-gradient(135deg,#dfe6ee,#2b4f78 55%,#0e2440)}
.statement-crescent{left:149px;top:2014px;width:276px;height:276px;border-radius:50%;background:var(--brand-blue)}
.statement-text{left:487px;top:2057px;width:561px;font-size:23px;line-height:38.5px;text-align:justify;color:#222}
.experience{left:0;top:2349px;width:1200px;height:405px;background:linear-gradient(180deg,#6d9bd0,#5c8bbf)}
.experience-title{left:0;top:2422px;width:1200px;text-align:center;color:var(--white)}
.partner{top:2532px;width:184px;height:112px;background:var(--white);display:flex;align-items:center;justify-content:center;gap:8px;font-size:24px;font-weight:700;color:var(--navy)}
.partner .sq{width:16px;height:16px;background:var(--steel)}
.dot{top:2709px;width:9px;height:9px;border-radius:50%;background:var(--white)}
.team{left:0;top:2754px;width:1200px;height:710px;background:var(--light)}
.team-title{left:0;top:2838px;width:1200px;text-align:center;color:var(--navy)}
.card{top:2977px;width:283px;height:341px;background:var(--white);border:1px solid #d5d9de;box-shadow:0 2px 4px rgba(0,0,0,.12);text-align:center}
.card svg{position:absolute;left:0;top:0}
.card .portrait{position:absolute;left:81px;top:-30px;width:120px;height:120px;border-radius:50%;background:linear-gradient(160deg,#c9b7a6,#3d4a5b);border:3px solid var(--white)}
.card .name{position:absolute;top:130px;width:100%;font-size:18px;color:#555;letter-spacing:.5px}
.card .role{position:absolute;top:158px;width:100%;font-size:15px;font-family:"Open Sans",sans-serif;color:#222}
.card .bio{position:absolute;top:194px;left:28px;width:227px;font-family:"Open Sans",sans-serif;font-size:14.5px;line-height:29px;color:#333}
.arrow{top:3155px;font-size:28px;color:#444}
.contact{left:0;top:3464px;width:1200px;height:406px;background:linear-gradient(90deg,#0e2540,#1d3e62)}
.contact-title{left:168px;top:3516px;font-size:28px;font-weight:700;color:var(--white)}
.contact-row{left:160px;display:flex;gap:26px;color:var(--white);font-family:"Open Sans",sans-serif;font-size:19px;line-height:32px}
.contact-icon{width:50px;height:50px;border-radius:50%;background:var(--white);flex:none;display:flex;align-items:center;justify-content:center}
.form-card{left:654px;top:3436px;width:384px;height:408px;background:var(--white)}
.form-title{top:30px;width:100%;text-align:center;font-size:28px;font-weight:700;color:var(--navy)}
.field{left:32px;width:321px;height:59px;border:1px solid #c9ccd0;font-family:"Open Sans",sans-serif;font-size:16px;color:#444;padding:18px 28px}
.submit{left:109px;top:328px;width:168px;height:48px;border-radius:24px;background:var(--navy);color:var(--white);font-size:19px;font-weight:700;text-align:center;line-height:48px}
.footer-links{left:0;top:3904px;width:1200px;display:flex;justify-content:center;gap:38px;font-size:17px;color:#222}
.footer-social{left:0;top:3946px;width:1200px;display:flex;justify-content:center;gap:16px}
.footer-social .social-dot{border-color:var(--navy)}
.copyright{left:0;top:3998px;width:1200px;text-align:center;font-size:16px;color:#222}
</style>
</head>
<body>

<div class="abs topbar">
  <div class="abs item" style="left:110px">
    <svg width="18" height="18" viewBox="0 0 24 24"><path fill="#fff" d="M6.6 10.8a15 15 0 0 0 6.6 6.6l2.2-2.2a1 1 0 0 1 1-.25 11.4 11.4 0 0 0 3.6.57 1 1 0 0 1 1 1V20a1 1 0 0 1-1 1A17 17 0 0 1 3 4a1 1 0 0 1 1-1h3.5a1 1 0 0 1 1 1c0 1.25.2 2.45.57 3.6a1 1 0 0 1-.25 1z"/></svg>
    <span>555-014-2290</span>
  </div>
  <div class="abs divider"></div>
  <div class="abs item" style="left:288px">
    <svg width="20" height="16" viewBox="0 0 24 18"><rect width="24" height="18" rx="2" fill="#fff"/><path d="M1 2l11 8 11-8" stroke="#0f2a44" stroke-width="2" fill="none"/></svg>
    <span>info@meridane.example</span>
  </div>
  <div class="abs social-dot" style="left:960px;top:8px"></div>
  <div class="abs social-dot" style="left:1006px;top:8px"></div>
  <div class="abs social-dot" style="left:1054px;top:8px"></div>
</div>

<header class="abs header">
  <div class="abs brand">
    <div class="brand-mark"></div>
    <div class="brand-name">MERIDANE</div>
    <div class="brand-sub">INDUSTRIES</div>
  </div>
  <span class="abs nav" style="left:448px">Home</span>
  <span class="abs nav" style="left:531px">About Us <i class="chev"></i></span>
  <span class="abs nav" style="left:640px">Investment Focus</span>
  <span class="abs nav" style="left:813px">Industry Focus <i class="chev"></i></span>
  <span class="abs nav" style="left:968px">Our Investment</span>
</header>

<section class="abs hero" role="img" aria-label="Stacks of coins in front of a city skyline with rising market chart lines">
  <h1>PARTNERING WITH EXCEPTIONAL LEADERS<br>BUILDING WORLD-CLASS COMPANIES</h1>
</section>

<h2 class="abs section-title about-title">About Us</h2>
<p class="abs about-text">Meridane Industries focuses on opportunities where it can support senior management to drive rapid growth and profit improvement through capital infusion, technology innovation and organizational expertise.&nbsp; We invest across a variety of growth industries with an emphasis on reshoring and rebuilding America.</p>
<div class="abs about-frame"></div>
<div class="abs about-photo" role="img" aria-label="Hand placing a coin beside a seedling growing from a pile of coins"></div>

<section class="abs focus" role="img" aria-label="Businessman holding a tablet with a glowing rising bar chart"></section>
<h2 class="abs section-title focus-title">Areas of Focus</h2>

<div class="abs focus-item" style="left:137px;top:1398px">
  <div class="focus-ring"><svg width="56" height="56" viewBox="0 0 56 56" fill="none" stroke="#0f2a44" stroke-width="2.5"><path d="M28 5l18 7v14c0 12-8 21-18 25C18 47 10 38 10 26V12z"/><circle cx="28" cy="25" r="5"/><path d="M28 30v8"/></svg></div>Defense</div>
<div class="abs focus-item" style="left:490px;top:1398px">
  <div class="focus-ring"><svg width="56" height="56" viewBox="0 0 56 56" fill="none" stroke="#0f2a44" stroke-width="2.5"><path d="M26 5l18 7v14c0 12-8 21-18 25C16 47 8 38 8 26V12z"/><rect x="32" y="32" width="16" height="13"/><path d="M35 32v-4a5 5 0 0 1 10 0v4"/></svg></div>cybersecurity</div>
<div class="abs focus-item" style="left:830px;top:1398px">
  <div class="focus-ring"><svg width="56" height="56" viewBox="0 0 56 56" fill="none" stroke="#0f2a44" stroke-width="2.5"><path d="M6 48V14h8v18l10-8v8l10-8v8l10-8v24z"/><rect x="14" y="38" width="6" height="5"/><rect x="28" y="38" width="6" height="5"/></svg></div>Industrial</div>
<div class="abs focus-item" style="left:137px;top:1646px">
  <div class="focus-ring"><svg width="56" height="56" viewBox="0 0 56 56" fill="none" stroke="#0f2a44" stroke-width="2.5"><rect x="16" y="16" width="24" height="24"/><rect x="23" y="23" width="10" height="10"/><path d="M22 16V8M28 16V8M34 16V8M22 40v8M28 40v8M34 40v8M16 22H8M16 28H8M16 34H8M40 22h8M40 28h8M40 34h8"/></svg></div>Digital Enterprise</div>
<div class="abs focus-item" style="left:490px;top:1646px">
  <div class="focus-ring"><svg width="56" height="56" viewBox="0 0 56 56" fill="none" stroke="#0f2a44" stroke-width="2.5"><circle cx="28" cy="16" r="6"/><path d="M28 22v14M28 28l-12-6M28 28l12-6M28 36l-10 10M28 36l10 10"/><circle cx="14" cy="21" r="3"/><circle cx="42" cy="21" r="3"/><circle cx="17" cy="47" r="3"/><circle cx="39" cy="47" r="3"/></svg></div>Technology</div>
<div class="abs focus-item" style="left:830px;top:1646px">
  <div class="focus-ring"><svg width="56" height="56" viewBox="0 0 56 56" fill="none" stroke="#0f2a44" stroke-width="2.5"><rect x="8" y="18" width="40" height="28"/><path d="M8 26h40M20 18v-6h16v6"/><circle cx="28" cy="34" r="5"/></svg></div>Professional</div>

<div class="abs statement-crescent"></div>
<div class="abs statement-photo" role="img" aria-label="Investor in a suit sketching a glowing market chart"></div>
<p class="abs statement-text">We place capital for long-term growth and revenue generation. Our investment horizon enables a focus on building strong sustainable companies, with empowered teams maximizing impact.</p>

<section class="abs experience" role="img" aria-label="Financial market numbers and coin stacks in blue tones"></section>
<h2 class="abs section-title experience-title">Investment Experience</h2>
<div class="abs partner" style="left:105px"><span class="sq"></span>Voltwise</div>
<div class="abs partner" style="left:302px"><span class="sq"></span>Cellgrove</div>
<div class="abs partner" style="left:499px"><span class="sq"></span>Halvern AI</div>
<div class="abs partner" style="left:696px"><span class="sq"></span>Plotline</div>
<div class="abs partner" style="left:893px"><span class="sq"></span>Tallow PR</div>
<div class="abs dot" style="left:578px"></div>
<div class="abs dot" style="left:596px"></div>
<div class="abs dot" style="left:614px"></div>

<section class="abs team"></section>
<h2 class="abs section-title team-title">Management Team</h2>
<span class="abs arrow" style="left:64px">‹</span>
<span class="abs arrow" style="left:1102px">›</span>

<div class="abs card" style="left:121px">
  <svg width="283" height="100"><path d="M0 26 L283 26 Q205 36 170 92 L112 92 Q78 36 0 26Z" fill="#3b4650"/></svg>
  <div class="portrait" role="img" aria-label="Portrait of Daniel Penwarden"></div>
  <div class="name">DANIEL PENWARDEN</div>
  <div class="role">Partner at Meridane Industries</div>
  <p class="bio">He additionally serves as the Founding Partner of the single family office and advisory firm Penwarden Quill Partners.</p>
</div>
<div class="abs card" style="left:454px">
  <svg width="283" height="100"><path d="M0 26 L283 26 Q205 36 170 92 L112 92 Q78 36 0 26Z" fill="#3b4650"/></svg>
  <div class="portrait" role="img" aria-label="Portrait of Lena Marwick"></div>
  <div class="name">LENA MARWICK</div>
  <div class="role">Partner at Meridane Industries</div>
  <p class="bio">An experienced investor, Lena's investment portfolio spans across real estate, cyber security, blockchain,</p>
</div>
<div class="abs card" style="left:789px">
  <svg width="283" height="100"><path d="M0 26 L283 26 Q205 36 170 92 L112 92 Q78 36 0 26Z" fill="#3b4650"/></svg>
  <div class="portrait" role="img" aria-label="Portrait of Rafiq Anwar"></div>
  <div class="name">RAFIQ ANWAR</div>
  <div class="role">Founding at Meridane Industries</div>
  <p class="bio">A seasoned investment professional, Rafiq has more than 14 years buy and sell side experience in the capital.</p>
</div>

<section class="abs contact" role="img" aria-label="Dark blue city and finance backdrop"></section>
<h2 class="abs contact-title">Contact us</h2>
<div class="abs contact-row" style="top:3584px">
  <div class="contact-icon"><svg width="20" height="24" viewBox="0 0 20 24"><path d="M10 0a8 8 0 0 1 8 8c0 6-8 16-8 16S2 14 2 8a8 8 0 0 1 8-8z" fill="#0f2a44"/><circle cx="10" cy="8" r="3" fill="#fff"/></svg></div>
  <span>Lorem ipsum dolor sit<br>amet, consectetur<br>adipiscing elit,</span>
</div>
<div class="abs contact-row" style="top:3694px">
  <div class="contact-icon"><svg width="20" height="20" viewBox="0 0 24 24"><path fill="#0f2a44" d="M6.6 10.8a15 15 0 0 0 6.6 6.6l2.2-2.2a1 1 0 0 1 1-.25 11.4 11.4 0 0 0 3.6.57 1 1 0 0 1 1 1V20a1 1 0 0 1-1 1A17 17 0 0 1 3 4a1 1 0 0 1 1-1h3.5a1 1 0 0 1 1 1c0 1.25.2 2.45.57 3.6a1 1 0 0 1-.25 1z"/></svg></div>
  <span style="line-height:50px">(555) 014-2290</span>
</div>
<div class="abs contact-row" style="top:3778px">
  <div class="contact-icon"><svg width="20" height="15" viewBox="0 0 24 18"><rect width="24" height="18" rx="2" fill="#0f2a44"/><path d="M1 2l11 8 11-8" stroke="#fff" stroke-width="2" fill="none"/></svg></div>
  <span style="line-height:50px">info@meridane.example</span>
</div>

<svg class="abs" style="left:620px;top:3436px" width="452" height="28"><path d="M0 28L34 0V28Z" fill="#3e556d"/><path d="M418 0L452 28H418Z" fill="#3e556d"/></svg>
<div class="abs form-card">
  <div class="abs form-title">Work with us</div>
  <div class="abs field" style="top:100px">Name</div>
  <div class="abs field" style="top:172px">Email</div>
  <div class="abs field" style="top:245px">Message</div>
  <div class="abs submit">SUBMIT</div>
</div>

<nav class="abs footer-links"><span>Home</span><span>About Us</span><span>Investment Focus</span><span>Industry Focus</span><span>Our Investment</span></nav>
<div class="abs footer-social"><div class="social-dot"></div><div class="social-dot"></div><div class="social-dot"></div></div>
<p class="abs copyright">Copyrights 2020 All rights reserved</p>

</body>
</html>
```